Flyer for the Radiant Harvest Worship Day

I am looking to create a flyer for a one day prayer retreat our church is organizing.
This flyer will be posted on social media, websites and will also be printed so it can be mailed to people.
I am looking for something professional, with good use of our logo and band colors (logo colors).
I am counting on the designer's skill, creativity, art and knowledge of media communication to produce a flyer that will effectively and quickly convey the message we are trying to spread.
CONTENT OF THE FLYER:
Event title: Radiant Harvest Worship Day
Date: Tuesday July 2nd, 2019
Time: 11:00AM - 7:00PM
Belmont Hotel, 4875 Maple Ridge Road, Portland, Maine 04219 (Room: Evergreen)
Event Key words to highlight what the event is about: Prayer, Sharing the Word, Panel discussion, prophecy, Impartation.
Key phrases:
A one day prayer retreat.
Jesus Chris is Lord
Contact info:
www.tuvela.org
Phone: 207 583 2194
Email: contact@brookmeadow.org

```html
<!DOCTYPE html>
<html lang="en">
<head>
<meta charset="utf-8">
<title>Radiant Harvest Worship Day – Flyer</title>
<link rel="stylesheet" href="https://fonts.googleapis.com/css2?family=Cinzel:wght@400&family=Lato:wght@400;700;900&family=Yellowtail&display=swap">
<style>
  :root {
    --navy: #0f3a5f;
    --orange: #f39322;
    --white: #ffffff;
    --ink: #222a35;
    --stage: #67696c;
    --sky-top: #8a909a;
    --sky-mid: #3b4b68;
    --sky-low: #161e2c;
    --earth: #060606;
    --panel-light: #ffffff;
    --panel-shade: #d6d7d9;
  }
  * { margin: 0; padding: 0; box-sizing: border-box; }
  html, body {
    width: 1042px;
    height: 1200px;
    overflow: hidden;
    background: var(--stage);
  }
  .flyer {
    position: absolute;
    left: 118px;
    top: 30px;
    width: 806px;
    height: 1140px;
    display: block;
  }
  .serif-caps { font-family: "Cinzel", serif; fill: var(--white); }
  .script { font-family: "Yellowtail", cursive; }
  .sans { font-family: "Lato", sans-serif; }
  .brand-name { font-size: 96px; letter-spacing: 2px; }
  .event-kicker { font-size: 58px; letter-spacing: 2px; }
  .event-title { font-size: 172px; fill: var(--orange); }
  .event-day { font-size: 118px; fill: var(--white); }
  .venue-name { font-size: 44px; font-weight: 900; fill: var(--white); }
  .venue-kind { font-size: 56px; font-weight: 400; fill: var(--orange); }
  .venue-address { font-size: 26px; font-weight: 400; fill: var(--white); }
  .agenda-item { font-size: 32px; font-weight: 900; fill: var(--navy); }
  .retreat-line { font-size: 42px; font-weight: 900; fill: var(--orange); }
  .retreat-motto { font-size: 82px; fill: var(--white); }
  .label { font-size: 40px; font-weight: 900; fill: var(--white); }
  .detail { font-size: 42px; font-weight: 700; fill: var(--ink); }
  .phone { font-size: 52px; font-weight: 900; fill: var(--navy); }
  .email { font-size: 36px; font-weight: 700; fill: var(--white); }
  .website { font-size: 40px; font-weight: 700; fill: var(--white); }
</style>
</head>
<body>
<svg class="flyer" viewBox="0 0 1324 1872" xmlns="http://www.w3.org/2000/svg" aria-label="Radiant Harvest Worship Day flyer">
  <defs>
    <linearGradient id="sky" x1="0" y1="0" x2="0" y2="1">
      <stop offset="0" stop-color="var(--sky-top)"/>
      <stop offset="0.45" stop-color="var(--sky-mid)"/>
      <stop offset="0.75" stop-color="var(--sky-low)"/>
      <stop offset="1" stop-color="var(--earth)"/>
    </linearGradient>
    <linearGradient id="hill" x1="0" y1="0" x2="0" y2="1">
      <stop offset="0" stop-color="#6e7370"/>
      <stop offset="0.6" stop-color="#2f3331"/>
      <stop offset="1" stop-color="#111"/>
    </linearGradient>
    <linearGradient id="panel" x1="0" y1="0" x2="1" y2="1">
      <stop offset="0" stop-color="var(--panel-light)"/>
      <stop offset="1" stop-color="var(--panel-shade)"/>
    </linearGradient>
    <clipPath id="sheet"><rect width="1324" height="1872"/></clipPath>
    <clipPath id="panel-shape">
      <path d="M780 1047 C950 1040 1180 960 1324 850 V1872 H710 C830 1650 850 1300 780 1047 Z"/>
    </clipPath>
  </defs>

  <g clip-path="url(#sheet)">
    <!-- base -->
    <rect class="sheet-base" width="1324" height="1872" fill="var(--navy)"/>

    <!-- hero photo area -->
    <path class="hero-photo" role="img" aria-label="Photo: man praying with folded hands against a cloudy evening sky over a dark field"
          d="M140 0 H1324 V775 C1180 900 1000 990 760 990 H140 Z" fill="url(#sky)"/>

    <!-- orange flame shape -->
    <path class="flame-band" fill="var(--orange)"
          d="M200 0 H225 C160 130 150 230 175 260 C60 350 30 480 60 600 C100 720 200 760 210 950 C215 1080 150 1170 0 1180 V1872 H640 C780 1600 830 1350 770 1030 C720 850 580 750 500 650 C420 560 340 480 300 400 C250 300 200 150 200 0 Z"/>

    <!-- white swoosh in navy drop -->
    <path class="swoosh" fill="var(--white)"
          d="M115 700 C200 850 215 1060 0 1090 V1130 C245 1115 225 850 115 700 Z"/>

    <!-- bottom-left photo disc -->
    <circle cx="220" cy="1830" r="395" fill="var(--orange)"/>
    <circle cx="220" cy="1830" r="380" fill="var(--navy)"/>
    <circle class="crosses-photo" role="img" aria-label="Photo: three wooden crosses silhouetted on a misty hill"
            cx="220" cy="1830" r="368" fill="url(#hill)"/>

    <!-- right info panel with bands -->
    <path class="panel-edge-orange" fill="none" stroke="var(--orange)" stroke-width="22"
          d="M700 1000 C950 1000 1160 920 1340 770"/>
    <path class="panel-edge-navy" fill="var(--navy)"
          d="M745 1020 C950 1015 1170 930 1324 815 V1872 H675 C800 1650 820 1300 745 1020 Z"/>
    <path class="info-panel" fill="url(#panel)"
          d="M780 1047 C950 1040 1180 960 1324 850 V1872 H710 C830 1650 850 1300 780 1047 Z"/>
    <rect class="contact-bar" x="600" y="1675" width="724" height="152" fill="var(--orange)" clip-path="url(#panel-shape)"/>

    <!-- brand -->
    <text class="serif-caps brand-name" x="949" y="255" text-anchor="middle">TUVELA</text>

    <!-- event title -->
    <text class="serif-caps event-kicker" x="966" y="472" text-anchor="middle">RADIANT HARVEST</text>
    <text class="script event-title" x="945" y="627" text-anchor="middle" textLength="570" lengthAdjust="spacingAndGlyphs">Worship</text>
    <text class="script event-day" x="728" y="737">Day</text>

    <!-- venue badge -->
    <circle cx="389" cy="682" r="195" fill="var(--navy)"/>
    <circle cx="389" cy="682" r="182" fill="none" stroke="var(--white)" stroke-width="4" stroke-dasharray="12 7"/>
    <g class="venue sans" text-anchor="middle">
      <text class="venue-name" x="389" y="617">BELMONT</text>
      <text class="venue-kind" x="389" y="684">HOTEL</text>
      <text class="venue-address" x="389" y="724">4875 Maple Ridge Road,</text>
      <text class="venue-address" x="389" y="756">Portland, Maine 04219</text>
      <text class="venue-address" x="389" y="788">(Room: Evergreen)</text>
    </g>

    <!-- agenda -->
    <g class="agenda sans">
      <g fill="var(--navy)">
        <path d="M262 925 L275 925 L288 942 L275 959 L262 959 L275 942 Z"/>
        <path d="M262 978 L275 978 L288 995 L275 1012 L262 1012 L275 995 Z"/>
        <path d="M262 1031 L275 1031 L288 1048 L275 1065 L262 1065 L275 1048 Z"/>
        <path d="M262 1084 L275 1084 L288 1101 L275 1118 L262 1118 L275 1101 Z"/>
        <path d="M262 1138 L275 1138 L288 1155 L275 1172 L262 1172 L275 1155 Z"/>
      </g>
      <text class="agenda-item" x="302" y="954">PRAYER</text>
      <text class="agenda-item" x="302" y="1007">SHARING THE WORD</text>
      <text class="agenda-item" x="302" y="1060">PANEL DISCUSSION</text>
      <text class="agenda-item" x="302" y="1113">PROPHECY</text>
      <text class="agenda-item" x="302" y="1167">IMPARTATION</text>
    </g>

    <!-- retreat banner -->
    <rect class="retreat-box" x="66" y="1240" width="688" height="245" rx="18" fill="var(--navy)"/>
    <text class="sans retreat-line" x="410" y="1325" text-anchor="middle">A ONE DAY PRAYER RETREAT</text>
    <text class="script retreat-motto" x="406" y="1428" text-anchor="middle">Jesus Chris is Lord</text>

    <!-- date -->
    <rect x="901" y="1135" width="348" height="209" fill="none" stroke="var(--navy)" stroke-width="3"/>
    <rect x="964" y="1100" width="223" height="67" rx="20" fill="var(--navy)"/>
    <g class="sans" text-anchor="middle">
      <text class="label" x="1076" y="1148">DATE</text>
      <text class="detail" x="1075" y="1229">Tuesday</text>
      <text class="detail" x="1075" y="1285">July 2nd, 2019</text>
    </g>

    <!-- time -->
    <rect x="891" y="1417" width="348" height="210" fill="none" stroke="var(--navy)" stroke-width="3"/>
    <rect x="954" y="1383" width="223" height="66" rx="20" fill="var(--navy)"/>
    <g class="sans" text-anchor="middle">
      <text class="label" x="1066" y="1431">TIME</text>
      <text class="detail" x="1065" y="1512">11:00AM</text>
      <text class="detail" x="1065" y="1567">to 7:00PM</text>
    </g>

    <!-- contact -->
    <path class="phone-icon" fill="var(--white)"
          d="M852 1702 l12 -4 l12 22 l-9 8 c4 10 10 17 20 22 l8 -9 l22 12 l-4 12 c-2 6 -8 9 -14 8 c-28 -6 -46 -26 -53 -54 c-1 -7 2 -14 6 -17 z"/>
    <text class="sans phone" x="899" y="1745">207 583 2194</text>
    <text class="sans email" x="1044" y="1795" text-anchor="middle">contact@brookmeadow.org</text>
    <text class="sans website" x="97" y="1793">www.tuvela.org</text>
  </g>
</svg>
</body>
</html>
```